Modern Small Law Firm Website To Look Cutting Edge

I need a website design for a new, single-attorney law firm. The firm will be called "The Thornwell Law Group." Our goal is to handle car accident and general personal injury lawsuits for individuals.

Our selling points are: (1) We charge less so you keep more; (2) We have experience and success trying and settling multi-million dollar cases; (3) We use modern technology to make the whole process simple, easy and hassle-free for clients.

Also because we are a one-man law firm, the clients will personally know the lawyer and have access to them. For that reason, I thought a good big tagline for the website would be "KNOW YOUR LAWYER"

I like the idea of splitting the website vertically down the middle, with the left side having a blue background, a picture of me, and big white lettering for the tagline, and the right side having a white background with blue lettering and headlines. I don't want navy blue or royal blue, but a more bright and eye-catching blue color. We can experiment with different shades.

I would be curious about how it could look with some minor orange accent coloring somewhere.

I need to feature prominently, probably in the top left corner, this phone number: 504-917-2083.

This will be used as much by mobile users as it would be by desktop/computer users.

The final design should communicate trust, convenience and cutting edge technology that leads to success.

Finally, I would be curious how we can have a sleek looking info submission box somewhere on the right side nearer the bottom that features different combinations of presenting these phrases: "QUICK QUESTION? QUICK ANSWER" The info submission button could say "Ask"

I am uploading two different pictures of me that can be used. The gray backgrounds are not necessary or good, if there is a way to cut them out that would be great. I can try and get that if needed.

Target Market(s)

Individuals who have been hurt by others, mostly in car accidents. They will be frustrated, inconvenienced and need to be soothed.

Industry/Entity Type

Legal

Number of Pages Required

1 page

Font styles to use
Sans Serif

Colors
0692cd
33a6d7
85cae6
faa54b
f78f20
3276b5

Requirements
Must have
• If you have started designing already, please note that the project description information is more important than the image that I uploaded originally. It has since been deleted.
• Also please now use the color photo that has been uploaded.
Nice to have
• I really want a clean and simple website design with not a lot of clutter. I'd like to avoid the typical law firm websites that you see that have tool bars across the top and basic borders/columns everywhere. It needs to grab your attention and look a little more cutting edge and different.
• Let's experiment with different eye-catching ways to present the three value propositions I noted.
• Also if the screen is split vertically with the left and right side being blue and white, maybe we can experiment with different ways that the two colors could fade into each other as opposed to just a line where one color starts and the other ends.
• And maybe the blue/white backgrounds could be textured somehow so that they don't appear flat. Perhaps we could try using differing shades of blue to give the appearance of pattern or 3D texture.
Should not have
• The basic picture/design I uploaded is just a suggestion, but there isn't really anything there.

```html
<!DOCTYPE html>
<html lang="en">
<head>
<meta charset="utf-8">
<title>The Thornwell Law Group</title>
<link href="https://fonts.googleapis.com/css2?family=Arimo:wght@400;700&display=swap" rel="stylesheet">
<style>
  :root {
    --brand-blue: #1a5aa6;
    --bright-blue: #1192e8;
    --footer-blue: #125aa0;
    --accent-orange: #e07b5b;
    --muted-grey: #a9a9a9;
    --white: #ffffff;
    --link-blue: #1e9be0;
  }
  * { margin: 0; padding: 0; box-sizing: border-box; }
  html, body { width: 882px; height: 1200px; overflow: hidden; }
  body { font-family: "Arimo", Arial, sans-serif; background: var(--white); position: relative; }
  .abs { position: absolute; }

  /* Hero */
  .hero { position: absolute; left: 0; top: 0; width: 882px; height: 318px; overflow: hidden; }
  .hero-photo {
    position: absolute; inset: 0;
    background: linear-gradient(100deg, #b45a7e 0%, #7d6aa8 28%, #5a6fb0 50%, #3a4f8a 72%, #14254f 100%);
  }
  .hero-portrait {
    position: absolute; left: 205px; top: 50px; width: 200px; height: 268px;
    background: linear-gradient(180deg, #4a3b3a 0%, #2a2a30 40%, #1d1e26 100%);
    border-radius: 90px 90px 0 0; opacity: .85;
  }
  .brand { left: 228px; top: 14px; color: var(--white); font-weight: 700; font-size: 13px; letter-spacing: .6px; }
  .phone-top { left: 588px; top: 6px; color: var(--white); font-weight: 700; font-size: 9px; letter-spacing: .8px; }
  .nav { left: 510px; top: 25px; display: flex; gap: 20px; font-size: 6.5px; color: #d8def0; }
  .nav .active { color: var(--white); font-weight: 700; }
  .tagline { left: 416px; top: 112px; color: var(--white); font-weight: 700; font-size: 48px; line-height: 54px; letter-spacing: -.5px; }
  .attorney { left: 419px; top: 273px; color: var(--white); font-weight: 700; font-size: 11px; }

  /* Reasons */
  .reasons-title { left: 0; width: 882px; top: 357px; text-align: center; color: var(--brand-blue); font-size: 17px; }
  .reason { width: 125px; text-align: center; color: var(--muted-grey); font-size: 10.5px; line-height: 13px; }
  .reason-icon { position: absolute; }

  /* Question form */
  .ask-band { left: 0; top: 540px; width: 882px; height: 295px; background: var(--bright-blue); }
  .ask-title { left: 219px; top: 579px; color: var(--white); font-size: 16px; }
  .ask-intro { left: 219px; top: 608px; width: 300px; color: var(--white); font-size: 7.6px; line-height: 12px; }
  .field { border: 1px solid rgba(255,255,255,.85); color: var(--white); font-size: 7.6px; padding: 8px 12px; }
  .ask-button { left: 387px; top: 786px; width: 95px; height: 29px; background: var(--accent-orange); color: var(--white); font-weight: 700; font-size: 14px; display: flex; align-items: center; justify-content: center; }

  /* Testimonial */
  .quote { left: 261px; width: 360px; top: 902px; text-align: center; color: var(--brand-blue); font-size: 11px; line-height: 16.5px; }
  .quote-name { left: 0; width: 869px; top: 965px; text-align: center; color: var(--link-blue); font-weight: 700; font-size: 7.6px; }
  .quote-role { left: 0; width: 869px; top: 978px; text-align: center; color: var(--muted-grey); font-size: 7.6px; }

  /* Footer */
  .footer { left: 0; top: 1025px; width: 882px; height: 175px; background: var(--footer-blue); }
  .footer-heading { color: var(--white); font-weight: 700; font-size: 11px; letter-spacing: .6px; }
  .footer-text { color: var(--white); font-size: 7.6px; line-height: 12.5px; }
  .footer-address { color: var(--white); font-size: 11px; line-height: 13.5px; }
  .footer-contact { color: var(--white); font-size: 8px; letter-spacing: .6px; line-height: 10.5px; }
  .copyright { left: 302px; top: 1168px; width: 250px; color: var(--white); font-size: 6px; line-height: 8px; letter-spacing: .3px; }
</style>
</head>
<body>

<header class="hero">
  <div class="hero-photo" role="img" aria-label="Evening street scene with wrought-iron balconies and city lights behind the attorney"></div>
  <div class="hero-portrait" role="img" aria-label="Portrait of attorney Daniel Thornwell in a dark suit and striped tie"></div>
  <div class="abs brand">The Thornwell Law Group</div>
  <div class="abs phone-top">504-917-2083</div>
  <nav class="abs nav"><span class="active">HOME</span><span>SERVICES</span><span>CONTACT US</span></nav>
  <h1 class="abs tagline">KNOW<br>YOUR<br>LAWYER</h1>
  <div class="abs attorney">Daniel Thornwell</div>
</header>

<section>
  <h2 class="abs reasons-title" style="font-weight:400">Why Choose The Thornwell Law Group</h2>

  <svg class="reason-icon" style="left:275px;top:389px" width="37" height="37" viewBox="0 0 37 37" fill="none" stroke="#1a5aa6" stroke-width="2.6">
    <circle cx="18.5" cy="18.5" r="16.5"/>
    <path d="M23 12.5c-1-1.3-2.6-2-4.5-2-2.6 0-4.3 1.4-4.3 3.3 0 4.4 9 2.4 9 7 0 2-1.8 3.4-4.6 3.4-2 0-3.7-.8-4.7-2.2M18.5 8v3M18.5 25v4"/>
  </svg>
  <svg class="reason-icon" style="left:414px;top:389px" width="37" height="37" viewBox="0 0 37 37" fill="none" stroke="#1a5aa6" stroke-width="2.6">
    <circle cx="18.5" cy="18.5" r="16.5"/>
    <path d="M18.5 9v10l5 4.5"/>
  </svg>
  <svg class="reason-icon" style="left:565px;top:395px" width="37" height="26" viewBox="0 0 37 26" fill="none" stroke="#1a5aa6" stroke-width="1.4">
    <rect x="4" y="2" width="29" height="18"/>
    <path d="M1 23h35"/>
  </svg>

  <p class="abs reason" style="left:231px;top:456px">We charge less so you keep more.</p>
  <p class="abs reason" style="left:372px;top:446px">We have experience and success trying and settling multi-million dollar cases</p>
  <p class="abs reason" style="left:513px;top:439px">We use modern technology to make the whole process simple, easy and hassle-free for clients</p>
</section>

<section class="abs ask-band"></section>
<h2 class="abs ask-title" style="font-weight:400">Quick Question? Quick Answer</h2>
<p class="abs ask-intro">Lorem ipsum dolor sit amet, consectetur adipiscing elit. Etiam ornare egestas dui, nec vestibulum diam bibendum et. Maecenas a elementum odio.</p>
<div class="abs field" style="left:219px;top:645px;width:136px;height:28px">Name</div>
<div class="abs field" style="left:367px;top:645px;width:136px;height:28px">Email</div>
<div class="abs field" style="left:514px;top:645px;width:137px;height:28px">Phone Number</div>
<div class="abs field" style="left:219px;top:681px;width:432px;height:83px;padding-top:11px">Message</div>
<div class="abs ask-button">Ask</div>

<section>
  <svg class="abs" style="left:413px;top:857px" width="38" height="36" viewBox="0 0 38 36" fill="none" stroke="#1a5aa6" stroke-width="2">
    <path d="M5 1.5h28a3.5 3.5 0 0 1 3.5 3.5v19a3.5 3.5 0 0 1-3.5 3.5H26l-6 6-2-6H5A3.5 3.5 0 0 1 1.5 24V5A3.5 3.5 0 0 1 5 1.5z"/>
    <circle cx="11" cy="14.5" r="1.6" fill="#1a5aa6" stroke="none"/>
    <circle cx="19" cy="14.5" r="1.6" fill="#1a5aa6" stroke="none"/>
    <circle cx="27" cy="14.5" r="1.6" fill="#1a5aa6" stroke="none"/>
  </svg>
  <blockquote class="abs quote">"Lorem ipsum dolor sit amet, consectetur adipiscing elit. Nullam quis eros sed lorem dignissim convallis. Duis consectetur libero in bibendum scelerisque."</blockquote>
  <div class="abs quote-name">Marcus Odell</div>
  <div class="abs quote-role">Graphic Designer</div>
</section>

<footer class="abs footer"></footer>
<div class="abs footer-heading" style="left:228px;top:1058px">The Thornwell Law Group</div>
<p class="abs footer-text" style="left:228px;top:1079px;width:170px">Lorem ipsum dolor sit amet, consectetur adipiscing elit. Nullam quis eros sed lorem dignissim convallis.</p>
<div class="abs footer-heading" style="left:500px;top:1058px">Location</div>
<p class="abs footer-address" style="left:500px;top:1085px">418 Magnolia Street<br>New Orleans, LA 70130</p>
<p class="abs footer-contact" style="left:500px;top:1123px">Phone: 504-917-2083<br>Fax: 504-917-2085</p>
<p class="abs copyright">The Thornwell Law Group © 2016, All Rights Reserved.</p>

</body>
</html>
```